Design Labels and Brand Look For Mens Soap Company

We are developing a mens soap line for a natural body wash and exfoliating bar. We will be selling this with our line of mens toiletry bags that we sell under the name of Corvane Totes on Quillmart. We are looking for you to design the product brand look with brand color palette and fonts.

The title for the mens body was is "Body Wash For Men". The title for the soap bar is "Exfoliating Bar Soap For Men"

We are providing the templates for these 2 items in PDF form. The final version of the design needs to be in a layered PSD format. You also need to send us the fonts used.

This soap will be sold on Quillmart. Do a search for "men's body wash" and "mens soap bar" you will see our competition on page one. We need to stand out with colors and design differentiaon.

Target Market(s)

Men

Industry/Entity Type

Skin Care Product

Requirements
Must have
• Layered PSD file with all fonts

```html
<!DOCTYPE html>
<html lang="en">
<head>
<meta charset="utf-8">
<title>Corvane Body Wash For Men – Labels</title>
<link rel="stylesheet" href="https://fonts.googleapis.com/css2?family=Russo+One&family=Michroma&family=Roboto+Condensed:wght@400;500&family=Open+Sans:wght@400;600&display=swap">
<style>
  :root {
    --page: #ffffff;
    --label-deep: #05070a;
    --label-mid: #0d1b25;
    --label-teal: #1d3a4a;
    --title: #9cc3d2;
    --title-light: #c9e1ea;
    --accent: #3ea6c9;
    --net: #7cc6e0;
    --ink: #ffffff;
    --ink-soft: #d7dde1;
    --bevel: #a9c4d1;
  }
  * { margin: 0; padding: 0; box-sizing: border-box; }
  html, body { width: 751px; height: 1200px; overflow: hidden; background: var(--page); }
  .sheet { position: relative; width: 751px; height: 1200px; }

  .label {
    position: absolute;
    height: 311px;
    overflow: hidden;
    color: var(--ink);
  }
  .label--standard { left: 88px; top: 272px; width: 580px; }
  .label--three-in-one { left: 76px; top: 617px; width: 592px; }

  .label__backdrop {
    position: absolute; inset: 0;
    background:
      linear-gradient(135deg, transparent 30%, rgba(29,58,74,.55) 45%, transparent 60%),
      linear-gradient(225deg, transparent 30%, rgba(29,58,74,.45) 45%, transparent 60%),
      radial-gradient(ellipse at 50% 20%, var(--label-mid), var(--label-deep) 75%);
  }
  .label__bevels { position: absolute; inset: 0; width: 100%; height: 100%; }

  .front {
    position: absolute; top: 0; width: 240px; height: 100%;
    transform: translateX(-50%);
    text-align: center;
  }
  .label--standard .front { left: 291px; }
  .label--three-in-one .front { left: 297px; }

  .brand {
    position: absolute; top: 52px; left: 0; right: 0;
    font-family: "Open Sans", sans-serif; font-weight: 600;
    font-size: 24px; color: var(--ink); letter-spacing: .5px;
  }
  .title {
    position: absolute; left: 0; right: 0;
    font-family: "Russo One", sans-serif;
    font-size: 27px; line-height: 22px; letter-spacing: 1px;
    color: var(--title);
    text-shadow: 0 1px 0 var(--title-light);
  }
  .label--standard .title { top: 138px; }
  .label--three-in-one .title { top: 138px; }
  .subtitle {
    position: absolute; left: 0; right: 0;
    font-family: "Michroma", sans-serif; font-size: 8px; letter-spacing: 6px;
    color: var(--ink-soft);
  }
  .label--standard .subtitle { top: 186px; }
  .label--three-in-one .subtitle { top: 187px; }

  .tagline {
    position: absolute; top: 212px; left: 0; right: 0;
    font-family: "Roboto Condensed", sans-serif; font-size: 6px; line-height: 7.5px;
    color: var(--ink-soft);
  }
  .claim { position: absolute; top: 202px; left: 0; right: 0; }
  .claim__name {
    font-family: "Michroma", sans-serif; font-size: 9px; letter-spacing: 1px;
    color: var(--accent);
  }
  .claim__uses {
    margin-top: 1px;
    font-family: "Roboto Condensed", sans-serif; font-size: 6px; color: var(--ink-soft);
  }
  .claim__oils {
    margin-top: 8px;
    font-family: "Roboto Condensed", sans-serif; font-size: 5px; line-height: 7.5px; color: var(--ink-soft);
  }

  .volume {
    position: absolute; top: 273px; left: 0; right: 0;
    font-family: "Roboto Condensed", sans-serif;
  }
  .volume__label { font-size: 6px; font-weight: 500; color: var(--net); }
  .volume__amount { font-size: 8px; color: var(--ink); }

  .side {
    position: absolute; top: 155px;
    font-family: "Open Sans", sans-serif; color: var(--ink);
  }
  .side--maker {
    width: 200px; text-align: center;
    font-size: 8px; line-height: 12px;
    transform: translate(-50%, -50%) rotate(90deg);
  }
  .label--standard .side--maker { left: 40px; }
  .label--three-in-one .side--maker { left: 38px; }
  .side--usage {
    width: 255px;
    transform: translate(-50%, -50%) rotate(-90deg);
  }
  .label--standard .side--usage { left: 519px; top: 152px; }
  .label--three-in-one .side--usage { left: 521px; top: 152px; }
  .usage__directions { font-size: 8px; line-height: 11px; }
  .usage__ingredients { margin-top: 7px; font-size: 7.2px; line-height: 10px; }
</style>
</head>
<body>
<main class="sheet">

  <section class="label label--standard" aria-label="Body wash label">
    <div class="label__backdrop" role="img" aria-label="Dark navy textured background with angled teal panels"></div>
    <svg class="label__bevels" viewBox="0 0 580 311" aria-hidden="true">
      <polyline points="182,85 291,128 400,85" fill="none" stroke="var(--bevel)" stroke-width="1.5"/>
      <polyline points="235,275 291,258 347,275" fill="none" stroke="var(--bevel)" stroke-width="1.2"/>
    </svg>
    <div class="front">
      <div class="brand">Corvane</div>
      <h1 class="title">BODY<br>WASH</h1>
      <p class="subtitle">FOR MEN</p>
      <p class="tagline">Lorem Ipsum is simply<br>dummy text of the printing and<br>typesetting industry.</p>
      <div class="volume">
        <div class="volume__label">Net wt.</div>
        <div class="volume__amount">16 FL OZ (473 ML)</div>
      </div>
    </div>
    <div class="side side--maker">
      (Business Name &amp; Contact Information)<br>
      (incl. address with zip code &amp; telephone)<br>
      Made in Usa
    </div>
    <div class="side side--usage">
      <p class="usage__directions">Pour a small amount of our luxurious hand soap into the palm of your hands and rub together under water for rich, cleaning lather.</p>
      <p class="usage__ingredients">Contains: Water, Sodium Laureth Sulfate, Vegetable Glycerine, Additives, Sodium Chloride, Fragnance, Citric Acid, Sodium Benzoate, Potassium Sorbate, Vitamin E, Cocoa Butter, Shea Butter, Virgin Olive Oil, Grapeseed Oil, Colors</p>
    </div>
  </section>

  <section class="label label--three-in-one" aria-label="Three in one body wash label">
    <div class="label__backdrop" role="img" aria-label="Dark navy textured background with angled teal panels"></div>
    <svg class="label__bevels" viewBox="0 0 592 311" aria-hidden="true">
      <polyline points="188,85 297,128 406,85" fill="none" stroke="var(--bevel)" stroke-width="1.5"/>
      <polyline points="241,275 297,258 353,275" fill="none" stroke="var(--bevel)" stroke-width="1.2"/>
    </svg>
    <div class="front">
      <div class="brand">Corvane</div>
      <h1 class="title">BODY<br>WASH</h1>
      <p class="subtitle">FOR MEN</p>
      <div class="claim">
        <div class="claim__name">3 IN 1 WASH</div>
        <div class="claim__uses">HAIR - FACE - BODY</div>
        <div class="claim__oils">With Shea Butter, Cocoa Butter,<br>Grapeseed Oil, Jojoba Oil</div>
      </div>
      <div class="volume">
        <div class="volume__label">Net wt.</div>
        <div class="volume__amount">16 FL OZ (473 ML)</div>
      </div>
    </div>
    <div class="side side--maker">
      (Business Name &amp; Contact Information)<br>
      (incl. address with zip code &amp; telephone)<br>
      Made in Usa
    </div>
    <div class="side side--usage">
      <p class="usage__directions">Pour a small amount of our luxurious hand soap into the palm of your hands and rub together under water for rich, cleaning lather.</p>
      <p class="usage__ingredients">Contains: Water, Sodium Laureth Sulfate, Vegetable Glycerine, Additives, Sodium Chloride, Fragnance, Citric Acid, Sodium Benzoate, Potassium Sorbate, Vitamin E, Cocoa Butter, Shea Butter, Virgin Olive Oil, Grapeseed Oil, Colors</p>
    </div>
  </section>

</main>
</body>
</html>
```